Stonebrook Glazeworks Inc. Business Card

Looking for business card with embossed raised logo print. Logo provided and want it to be most prominent image on card. Color pallet of black, red, white or charcoal gray preferred for brand recognition. Simple contact information on front and list description of services provided on back. Services included....Custom Showers, Tub Surrounds, Backsplashes, Fireplaces, Floors and more. Dustless Demolition, Lifetime Warranty, Proud member of the Federated Surface Installers Guild

Target Market(s)

High end residential remodel work and new home builders

Contact Information for Business Card

Phone # (402) 555-0193 email address, Stonebrookgw@mailvane.net Dorian Kovalski Owner

Requirements
Must have
• Business logo as most prominent image on the front of business card. Along with contact information and name Dorian Kovalski. Would like to see services provided on the back of the card.

```html
<!DOCTYPE html>
<html lang="en">
<head>
<meta charset="utf-8">
<title>Stonebrook Glazeworks Inc. Business Card</title>
<link rel="stylesheet" href="https://fonts.googleapis.com/css2?family=Arimo:wght@400;700&display=swap">
<style>
  :root {
    --backdrop: #4a4a4a;
    --card: #2b2b2b;
    --card-relief: #262626;
    --red: #e0262c;
    --white: #f4f4f4;
  }
  * { margin: 0; padding: 0; box-sizing: border-box; }
  html, body { width: 1200px; height: 963px; overflow: hidden; }
  body {
    position: relative;
    background: var(--backdrop);
    font-family: "Arimo", Arial, sans-serif;
    color: var(--white);
  }
  .card {
    position: absolute;
    top: 174px;
    width: 318px;
    height: 557px;
    background: var(--card);
  }
  .card-front { left: 222px; }
  .card-back { left: 636px; }

  /* front */
  .brand-mark {
    position: absolute;
    top: 90px;
    left: 50%;
    width: 52px;
    height: 52px;
    margin-left: -26px;
    background: var(--red);
  }
  .brand-name {
    position: absolute;
    left: 0; right: 0;
    text-align: center;
    color: var(--red);
    font-weight: 700;
    text-transform: uppercase;
    line-height: 1.15;
  }
  .card-front .brand-name { top: 168px; font-size: 24px; letter-spacing: 1px; }
  .person {
    position: absolute;
    top: 346px;
    left: 0; right: 0;
    text-align: center;
  }
  .person-name {
    color: var(--red);
    font-weight: 700;
    font-size: 19px;
    text-transform: uppercase;
  }
  .person-title { font-size: 15px; margin-top: 2px; }
  .contact-divider {
    position: absolute;
    top: 408px;
    left: 58px;
    width: 202px;
    height: 18px;
  }
  .contact-details {
    position: absolute;
    top: 445px;
    left: 0; right: 0;
    text-align: center;
    font-size: 15px;
    line-height: 20px;
  }

  /* back */
  .relief-field {
    position: absolute;
    top: 42px;
    left: 41px;
    width: 240px;
    height: 240px;
    background: var(--card-relief);
    box-shadow: inset 1px 1px 0 rgba(255,255,255,0.04), inset -1px -1px 0 rgba(0,0,0,0.3);
  }
  .card-back .brand-name {
    top: 324px;
    left: auto;
    right: 40px;
    text-align: right;
    font-size: 18px;
    letter-spacing: 0.5px;
  }
  .services {
    position: absolute;
    top: 375px;
    right: 40px;
    text-align: right;
    font-size: 15.5px;
    line-height: 20px;
  }
  .services-heading {
    color: var(--red);
    font-weight: 700;
    font-size: 17px;
    text-transform: uppercase;
    margin-bottom: 1px;
  }
  .services ul { list-style: none; }
</style>
</head>
<body>
  <section class="card card-front">
    <div class="brand-mark"></div>
    <div class="brand-name">Stonebrook<br>Glazeworks Inc.</div>

    <div class="person">
      <div class="person-name">Dorian Kovalski</div>
      <div class="person-title">Owner</div>
    </div>

    <svg class="contact-divider" viewBox="0 0 202 18" aria-hidden="true">
      <line x1="0" y1="9" x2="76" y2="9" stroke="#f4f4f4" stroke-width="1.2"/>
      <line x1="126" y1="9" x2="202" y2="9" stroke="#f4f4f4" stroke-width="1.2"/>
      <rect x="82" y="1" width="16" height="16" rx="3" fill="#e0262c"/>
      <path d="M86 5c0 5 4 9 9 9l1-2-2.5-1.5-1 1c-1.5-.7-2.8-2-3.5-3.5l1-1L88.5 4z" fill="#2b2b2b"/>
      <rect x="104" y="1" width="16" height="16" rx="3" fill="#e0262c"/>
      <rect x="106.5" y="5" width="11" height="8" fill="none" stroke="#2b2b2b" stroke-width="1.2"/>
      <polyline points="106.5,5 112,10 117.5,5" fill="none" stroke="#2b2b2b" stroke-width="1.2"/>
    </svg>

    <div class="contact-details">
      <div class="phone">(402) 555-0193</div>
      <div class="email">Stonebrookgw@mailvane.net</div>
    </div>
  </section>

  <section class="card card-back">
    <div class="relief-field"></div>
    <div class="brand-name">Stonebrook<br>Glazeworks Inc.</div>

    <div class="services">
      <div class="services-heading">Services</div>
      <ul>
        <li>Custom Showers</li>
        <li>Tub Surrounds | Backsplashes</li>
        <li>Fireplaces | Floors and more</li>
        <li>Dustless Demolition</li>
        <li>Lifetime Warranty</li>
        <li>Proud member of the Federated</li>
        <li>Surface Installers Guild</li>
      </ul>
    </div>
  </section>
</body>
</html>
```